Cinco de Mayo Event Poster- Los Cerritos

I need a poster for our restaurant, Los Cerritos, for Cinco de Mayo.
Final Size 11"x17"(portrait).
Use our official Los Cerritos Logo.
Date: Tuesday May 5
Live Music/ Mariachi/ DJ/ Ice Luge/ Beer Tent/ Giveaways.
Include our phone number 555-418-2936
Address : 47116 Garnet Rd, Livonia, MI 48150
website : www.loscerritoskitchen-demo.com

Industry/Entity Type

Restaurant

Colors
0054AA
0677BA
7BADD7
CADEEF
E8F1F8
0094D4
00A9DD
6FCCEA
C7EBF8
E9F6FB
00AB8E
00BBA5
67D7C9
C6EFE9
E9F9F6
FFC000
F8CF3A
FAE287
FDF2CF
FEFAEE
EE7325
F08F49
F5BC92
FAE3D3
FDF4ED
E54698
E96AAD
F1A4CE
F9D9EA
FCEFF6
A7469A
B969AE
D3A5CF
EDDBEB
F8F0F9
6B429C
8869AF
B7A5CE
E3DAEB
F3F0F8

Requirements
Must have
• Vereda Tequila Logo, Lumbral Tequila Logo.
Nice to have
• Palm Trees, margaritas, Mexican beer. I added our menus to give you a better Idea of who we are.vd
Should not have
• maracas/sombreros

```html
<!DOCTYPE html>
<html lang="en">
<head>
<meta charset="utf-8">
<title>Cinco de Mayo – Los Cerritos</title>
<link rel="stylesheet" href="https://fonts.googleapis.com/css2?family=Lilita+One&family=Archivo+Black&family=Montserrat:wght@700;800&display=swap">
<style>
  :root{
    --backdrop:#fc9a10;
    --sky-top:#4590d5;
    --sky-bottom:#4bb3d9;
    --ink:#0c2231;
    --sun:#ffc425;
    --tangerine:#f7a21b;
    --cream:#f8f8f2;
    --white:#ffffff;
    --sea:#1c87a3;
    --sand:#d9bd8a;
    --palm:#7fbfa6;
    --wood:#c08a5c;
    --brand:#c0392b;
    --gold:#b28b5a;
  }
  *{margin:0;padding:0;box-sizing:border-box}
  html,body{width:1200px;height:1200px;overflow:hidden}
  body{background:var(--backdrop);position:relative;font-family:"Montserrat",sans-serif}
  .poster{position:absolute;left:299px;top:138px;width:602px;height:930px;overflow:hidden;
    background:linear-gradient(180deg,var(--sky-top) 0%,var(--sky-bottom) 70%)}
  .corner{position:absolute;left:0;top:0}
  .partners{position:absolute;top:22px;right:16px;display:flex;gap:14px;align-items:center}
  .partner{font-family:"Lilita One",sans-serif;font-size:19px;color:var(--gold);letter-spacing:.5px}
  .partner-mark{display:flex;align-items:center;gap:5px}
  .partner-mark span.dot{width:10px;height:10px;border-radius:50%;background:var(--gold)}
  .brand{position:absolute;left:0;width:602px;top:95px;text-align:center;
    font-family:"Lilita One",sans-serif;font-size:34px;color:var(--brand);letter-spacing:.5px}
  .headline{position:absolute;left:30px;top:168px;font-family:"Lilita One",sans-serif;
    color:var(--ink);font-size:86px;line-height:70px;letter-spacing:2px;text-transform:uppercase}
  .weekday{position:absolute;left:60px;top:333px;font-family:"Lilita One",sans-serif;
    color:var(--ink);font-size:42px;letter-spacing:1.5px;text-transform:uppercase}
  .ribbon{position:absolute;left:28px;top:379px}
  .ribbon-text{position:absolute;left:60px;top:380px;width:208px;text-align:center;
    font-family:"Lilita One",sans-serif;font-size:38px;color:var(--ink);line-height:50px;letter-spacing:1px}
  .features{position:absolute;left:28px;top:460px;list-style:none;
    font-family:"Archivo Black",sans-serif;color:var(--white);font-size:25px;line-height:31.6px;text-transform:uppercase}
  .scene{position:absolute;left:0;top:648px;width:602px;height:204px;
    background:linear-gradient(180deg,#3aa3c4 0%,var(--sea) 60%,var(--sand) 88%)}
  .palms{position:absolute;left:300px;top:325px;width:302px;height:527px;
    background:linear-gradient(180deg,rgba(127,191,166,.85) 0%,rgba(127,191,166,.5) 25%,rgba(192,138,92,.75) 45%,rgba(192,138,92,.85) 100%);
    border-radius:60px 60px 0 0}
  .footer{position:absolute;left:0;top:852px;width:602px;height:78px;background:var(--sun);
    display:flex;align-items:center;color:var(--ink);font-weight:800;font-size:13px}
  .site{position:absolute;left:28px;font-size:12px;font-weight:700}
  .phone{position:absolute;left:260px;display:flex;align-items:center;gap:6px}
  .address{position:absolute;left:410px;display:flex;align-items:center;gap:8px;line-height:16px}
</style>
</head>
<body>
<main class="poster">
  <svg class="corner" width="602" height="200" viewBox="0 0 602 200" aria-hidden="true">
    <path d="M320 0 C420 60 520 110 602 120 L602 0 Z" fill="var(--cream)"/>
  </svg>
  <svg class="corner" width="602" height="200" viewBox="0 0 602 200" role="img" aria-label="Festive yellow bunting strung across the top">
    <path d="M0 64 C80 50 150 30 215 0 L225 12 C160 44 80 70 0 80 Z" fill="var(--sun)"/>
    <path d="M310 0 C400 62 500 115 602 130 L602 146 C490 134 390 86 300 14 Z" fill="var(--sun)"/>
  </svg>

  <div class="partners">
    <div class="partner">Vereda</div>
    <div class="partner-mark"><span class="dot"></span><span class="partner">Lumbral</span></div>
  </div>

  <div class="brand">Los Cerritos</div>

  <h1 class="headline">Cinco<br>de Mayo</h1>
  <div class="weekday">Tuesday</div>

  <svg class="ribbon" width="272" height="62" viewBox="0 0 272 62" aria-hidden="true">
    <polygon points="0,12 40,12 40,58 0,58 18,35" fill="var(--sun)"/>
    <polygon points="272,12 232,12 232,58 272,58 254,35" fill="var(--sun)"/>
    <polygon points="32,48 44,48 44,58" fill="#b3282d"/>
    <polygon points="240,48 228,48 228,58" fill="#b3282d"/>
    <rect x="32" y="0" width="208" height="50" fill="var(--tangerine)"/>
  </svg>
  <div class="ribbon-text">5th May</div>

  <ul class="features">
    <li>Live Music</li>
    <li>Mariachi</li>
    <li>DJ</li>
    <li>Ice Luge</li>
    <li>Beer Tent</li>
    <li>Giveaways</li>
  </ul>

  <div class="scene" role="img" aria-label="Turquoise sea with foamy waves meeting a sandy beach"></div>
  <div class="palms" role="img" aria-label="Two carved tiki-pole palm trees with green fronds standing on the beach"></div>

  <footer class="footer">
    <span class="site">www.loscerritoskitchen-demo.com</span>
    <span class="phone">
      <svg width="18" height="24" viewBox="0 0 18 24" aria-hidden="true"><path d="M4 1 L8 2 L8 8 L5 9 C5 14 7 17 10 19 L12 16 L17 18 L16 23 C8 23 1 15 1 6 Z" fill="var(--ink)"/></svg>
      555-418-2936
    </span>
    <span class="address">
      <svg width="18" height="26" viewBox="0 0 18 26" aria-hidden="true"><path d="M9 0 C4 0 0 4 0 9 C0 16 9 26 9 26 C9 26 18 16 18 9 C18 4 14 0 9 0 Z" fill="var(--ink)"/><circle cx="9" cy="9" r="3.5" fill="var(--sun)"/></svg>
      <span>47116 Garnet Rd<br>Livonia, MI 48150</span>
    </span>
  </footer>
</main>
</body>
</html>
```